Packaging Design Project for Wallaby Ridge Meats Company

Dusty Mates imports and distributes Australian Kangaroo Steak in the USA for Human Consumption. Kangaroo Steak is an Organic, High Protein, rich in Iron, low Fat Meat that Australians enjoy.

Kangaroo Meat is Promoted by Blue Canopy as an environmentally wise choice for health conscious diner.

Our Products give overseas consumers a chance to try what Australians enjoy and love!

The Packaging Design is for our Kangaroo Steaks which is sold on a 5 inch (height) x 7 inch (width) Tray.

The Tray has a plastic film cover on top covering the meat. This is what the design will Printed on.

The design should not exceed 43% of the Product Package Face, therefore leaving minimum of 57% of the Product visible through the clear part of the film.

We would like to see designs use the colors Orange, Green & Yellow. The use of other colors to highlight these colors are allowed. These are typical colors that represent the Australian Outback. It is not compulsory to use all of these colors, however we do want to keep our companies heritage and the label must keep and Australian theme.

Kangaroo Meat is an OUTBACK food.

Target Market(s)

Retail Consumers, Health Conscious Consumers, Vegetarians (they are called Kangatarians). Audience of Ages 25+

Industry/Entity Type

Plastic

Requirements
Must have
• The design must be sensitive to all audiences.
Points to Include
1. 98% Lean / 2% Fat
2. Low in Saturated Fat
3. High in Protein
4. High in Iron
5. Gluten Free
6. Kangaroo Meat is a 100% natural meat that is antibiotic, chemical & hormone free.
Kangaroo Meat is low in fat, high in protein, iron and minerals, and as such provides a food that promotes a healthy nutritional regime. (optional)
7. See back of Package for Easy Cooking Instructions
8. Fresh never Frozen
9. Grand Australian Redland Provisions
10. Dusty Mates Logo (not included)
11. Keep Refrigerated
12. www.dustymates.example

Should not have
• We do not want to see any pictures of Kangaroos on the label.

```html
<!DOCTYPE html>
<html lang="en">
<head>
<meta charset="utf-8">
<title>Kangaroo Steak Tray Label</title>
<link rel="stylesheet" href="https://fonts.googleapis.com/css2?family=Arimo:wght@400&display=swap">
<style>
  :root {
    --page: #ffffff;
    --label-black: #000000;
    --sun-core: #fff4b8;
    --sun-light: #fbe27a;
    --sun-mid: #f7b63a;
    --sun-deep: #ec7a1e;
    --sky-edge: #e2621a;
    --hills: #7a2c16;
    --ground: #c8692a;
    --ground-light: #d27a36;
    --earth-brown: #7c3f24;
    --text-white: #ffffff;
    --accent-orange: #f5a623;
  }
  html, body {
    margin: 0;
    width: 1200px;
    height: 900px;
    overflow: hidden;
    background: var(--page);
  }
  .canvas {
    position: relative;
    width: 1200px;
    height: 900px;
  }
  .label {
    position: absolute;
    left: 333px;
    top: 77px;
    width: 534px;
    height: 747px;
    background: var(--label-black);
    font-family: "Arimo", Arial, sans-serif;
    color: var(--text-white);
  }
  .outback-scene {
    position: absolute;
    left: 36px;
    top: 44px;
    width: 464px;
    height: 388px;
    border-radius: 26px 26px 0 0;
    overflow: hidden;
    background:
      radial-gradient(ellipse 70% 75% at 50% 86%, var(--sun-core) 0%, var(--sun-light) 22%, var(--sun-mid) 52%, transparent 80%),
      linear-gradient(180deg, var(--sky-edge) 0%, var(--sun-deep) 30%, var(--sun-mid) 70%);
  }
  .outback-scene .horizon-band {
    position: absolute;
    left: 0;
    right: 0;
    top: 298px;
    height: 36px;
    background: linear-gradient(180deg, rgba(122,44,22,0) 0%, var(--hills) 45%, var(--hills) 100%);
  }
  .outback-scene .ground-band {
    position: absolute;
    left: 0;
    right: 0;
    top: 334px;
    bottom: 0;
    background: linear-gradient(180deg, var(--ground-light) 0%, var(--ground) 100%);
  }
  .claims-panel {
    position: absolute;
    left: 18px;
    top: 425px;
    width: 504px;
    height: 204px;
    background: var(--earth-brown);
    border-radius: 10px 10px 60px 60px / 10px 10px 50px 50px;
    text-align: center;
    font-size: 17.5px;
    line-height: 22.5px;
    padding-top: 14px;
    box-sizing: border-box;
  }
  .claims-panel p { margin: 0; }
  .claims-panel .bullet {
    display: inline-block;
    width: 9px;
    height: 9px;
    border-radius: 50%;
    background: var(--accent-orange);
    margin: 0 2px 1px;
    vertical-align: middle;
  }
  .provisions-name {
    position: absolute;
    top: 634px;
    left: 0;
    width: 100%;
    text-align: center;
    color: var(--accent-orange);
    font-size: 19px;
  }
  .brand-logo {
    position: absolute;
    top: 664px;
    left: 0;
    width: 100%;
    text-align: center;
    font-size: 17.5px;
    line-height: 22px;
  }
  .footer-note {
    position: absolute;
    top: 708px;
    color: var(--accent-orange);
    font-size: 18px;
  }
  .storage { left: 18px; }
  .website { right: 10px; }
</style>
</head>
<body>
<div class="canvas">
  <section class="label">
    <div class="outback-scene" role="img" aria-label="Outback sunset illustration with radiating sun rays, birds in flight, silhouetted trees, distant hills and red earth">
      <div class="horizon-band" aria-hidden="true"></div>
      <div class="ground-band" aria-hidden="true"></div>
    </div>
    <div class="claims-panel">
      <p>98% Lean / 2% Fat <span class="bullet"></span>Low in Saturated Fat<span class="bullet"></span> High in Protein</p>
      <p>High in Iron<span class="bullet"></span> Gluten Free</p>
      <p>Kangaroo Meat is a 100% natural meat that is antibiotic, chemical &amp; hormone free. Kangaroo Meat is low in fat, high in protein, iron and minerals, and as such provides a food that promotes a healthy nutritional regime. (optional)</p>
      <p>See back of Package for Easy Cooking Instructions</p>
      <p>Fresh never Frozen</p>
    </div>
    <div class="provisions-name">Grand Australian Redland Provisions</div>
    <div class="brand-logo">Dusty Mates Logo<br>(not included)</div>
    <div class="footer-note storage">Keep Refrigerated</div>
    <div class="footer-note website">www.dustymates.example</div>
  </section>
</div>
</body>
</html>
```